New corporate stationery design for UK train leasing company

In advance of an office move later this year we are looking to redesign all our corporate stationery (business cards, letterhead, compliment slips, envelopes etc) as well as small branded items (such as mouse mats, drink mats, etc).

We wish to keep the same logo and corporate colours but are looking for a modern, fresh look that will tie in our stationery more with the look of our website and our PowerPoint template. We have a strapline, "Track Crews, True Knowhow" that we would like to incorporate into the stationery design and also need to include a "TEMLO" logo on the bottom of the letterhead/compliment slips. We have two offices so will need letterhead and compliment slips with both addresses.

The files attached include different versions of our logo (the main one is the black with green halo, file 1 or 3), our brand guidelines summary (including Pantone colours), the TEMLO logo and PowerPoint template.

More information about the business can be found at www.fernholtrail.co.uk.

If you have any questions please let me know.

I look forward to seeing the designs!
Regards
Moira

Target Market(s)

Main audience are train operators, rail industry suppliers, passenger transport groups, government and other political organisations, financiers/lenders.

Industry/Entity Type

Business

```html
<!DOCTYPE html>
<html lang="en">
<head>
<meta charset="utf-8">
<title>Fernhol Rail Stationery</title>
<link href="https://fonts.googleapis.com/css2?family=Arimo:wght@400;700&family=Michroma&display=swap" rel="stylesheet">
<style>
:root{
  --bg:#ececec;
  --paper:#ffffff;
  --ink:#4d4d4f;
  --teal:#1aa594;
  --band:#505052;
  --text:#333;
}
*{margin:0;padding:0;box-sizing:border-box}
html,body{width:1200px;height:937px;overflow:hidden;background:var(--bg);font-family:"Arimo",Arial,sans-serif;color:var(--text)}
.canvas{position:relative;width:1200px;height:937px}
.sheet{position:absolute;background:var(--paper)}
.accent{position:absolute;top:0;right:0;background:var(--teal)}
.brand{position:absolute;display:flex;align-items:center;gap:.3em;color:var(--ink);font-family:"Arimo",Arial,sans-serif;font-weight:400;white-space:nowrap;letter-spacing:-.01em}
.brand .dot{width:.5em;height:.5em;border-radius:50%;background:var(--teal);display:inline-block}
.url{font-family:"Michroma",sans-serif;color:#fff;letter-spacing:.12em;white-space:nowrap}
.band{position:absolute;display:flex;gap:3px}
.band > div{background:var(--band);display:flex;align-items:center;justify-content:center;flex-direction:column;color:#ddd}
.band .small{font-size:4.5px;line-height:1.4;text-align:center}

/* letterhead */
.letterhead{left:185px;top:66px;width:386px;height:546px}
.letterhead .accent{width:96px;height:13px}
.letter-body{position:absolute;left:36px;top:140px;width:300px;font-size:5.4px;line-height:1.45;color:#444}
.letter-body p{margin-bottom:9px}
.letter-body .gap{margin-bottom:24px}
.signature{width:24px;height:16px;background:linear-gradient(90deg,#bbb,#666);margin-bottom:6px}
.letterhead .band{left:8px;top:496px;width:370px;height:42px}
.letterhead .band > div:first-child{border-radius:6px 0 0 6px}
.letterhead .band > div:last-child{border-radius:0 6px 6px 0}

/* cover sheet */
.cover{left:636px;top:40px;width:458px;height:576px}
.cover .accent{width:130px;height:16px}
.cover .band{left:10px;top:542px;width:437px;height:21px}

/* business cards */
.card{width:177px;height:100px}
.card-front{left:45px;top:658px}
.card-back{left:45px;top:785px}
.card .accent{width:63px;height:8px}
.card .person{position:absolute;left:94px;top:20px;font-size:6.5px;font-weight:700;color:#333;line-height:1.3}
.card .person span{display:block;font-size:4.8px}
.card .band{left:7px;top:45px;width:162px;height:51px;gap:2px}
.card .band > div:first-child{border-radius:5px 0 0 5px}
.card .band > div:last-child{border-radius:0 5px 5px 0}
.card .band .small{font-size:3.6px}

/* compliment slip */
.slip{left:265px;top:672px;width:432px;height:207px}
.slip .accent{width:96px;height:12px}
.slip .address{position:absolute;left:14px;top:66px;font-size:8px;color:#333}
.slip .band{left:14px;top:176px;width:407px;height:22px}

/* envelope */
.envelope{left:737px;top:672px;width:431px;height:207px}
.envelope .flap{position:absolute;left:0;top:0;width:431px;height:72px;background:var(--band);border-radius:0 0 44px 44px;display:flex;align-items:center;justify-content:center}
</style>
</head>
<body>
<div class="canvas">

  <!-- Letterhead -->
  <section class="sheet letterhead">
    <div class="accent"></div>
    <div class="brand" style="left:18px;top:22px;font-size:22px">Fernhol Rail<span class="dot"></span></div>
    <div class="letter-body">
      <p>July 2, 2012</p>
      <p><b>Dear Sir,</b><br>Quay House, Dock St., Leeds</p>
      <p>is simply dummy text of the printing and typesetting industry. Lorem Ipsum has been the industry's standard dummy text ever since the 1500s, when an unknown printer took a galley of type and scrambled it to make a type specimen book. It has survived not only five centuries, but also the leap into electronic typesetting, remaining essentially unchanged. It was popularised in the 1960s with the release of Letraset sheets containing Lorem Ipsum passages, and more recently with desktop publishing software like Aldus PageMaker including versions of Lorem Ipsum.</p>
      <p class="gap">is simply dummy text of the printing and typesetting industry. Lorem Ipsum has been the industry's standard dummy text ever since the 1500s, when an unknown printer took a galley of type and scrambled it to make</p>
      <p>is simply dummy text of the printing and typesetting industry. Lorem Ipsum has been the industry's standard dummy text ever since the 1500s, when an unknown printer took a galley of type and scrambled it to make a type specimen book. It has survived not only five centuries, but also the leap into electronic typesetting, remaining essentially unchanged. It was popularised in the 1960s with the release of Letraset sheets containing Lorem Ipsum passages, and more recently with desktop publishing software like Aldus PageMaker including versions of Lorem Ipsum.</p>
      <p>Best Regards,</p>
      <div class="signature" role="img" aria-label="Handwritten signature"></div>
      <p><b>Daniel Rowe</b><br>Director<br><br>Quay House, Dock St., Leeds</p>
    </div>
    <div class="band">
      <div style="width:110px">
        <svg width="13" height="11" viewBox="0 0 24 20"><path d="M2 7c0-4 20-4 20 0v2h-5V7H7v2H2z M5 10h14l3 9H2z" fill="#fff"/></svg>
        <div class="small">020 7946 0123<br>020 7946 0124</div>
      </div>
      <div style="width:125px">
        <svg width="12" height="12" viewBox="0 0 24 24" fill="none" stroke="#fff" stroke-width="2"><circle cx="12" cy="12" r="10"/><ellipse cx="12" cy="12" rx="4" ry="10"/><path d="M2 12h20M4 7h16M4 17h16"/></svg>
        <div class="small">info@fernholtrail.co.uk<br>www.fernholtrail.co.uk</div>
      </div>
      <div style="width:129px">
        <svg width="9" height="12" viewBox="0 0 16 22"><path d="M8 0a8 8 0 0 1 8 8c0 6-8 14-8 14S0 14 0 8a8 8 0 0 1 8-8z" fill="#fff"/><circle cx="8" cy="8" r="3" fill="#505052"/></svg>
        <div class="small">12 Harbour Row<br>Leeds LS1 4AB</div>
      </div>
    </div>
  </section>

  <!-- Cover sheet -->
  <section class="sheet cover">
    <div class="accent"></div>
    <div class="brand" style="left:0;right:0;justify-content:center;top:238px;font-size:62px">Fernhol Rail<span class="dot"></span></div>
    <div class="band">
      <div style="width:119px"></div>
      <div class="url" style="width:195px;font-size:8.5px">www.fernholtrail.co.uk</div>
      <div style="width:117px;border-radius:0 4px 4px 0"></div>
    </div>
  </section>

  <!-- Business card front -->
  <section class="sheet card card-front">
    <div class="accent"></div>
    <div class="brand" style="left:6px;top:14px;font-size:13px">Fernhol<span class="dot"></span></div>
    <div class="person">OWEN HARTLEY<span>CREATIVE DIRECTOR</span></div>
    <div class="band">
      <div style="width:48px">
        <svg width="10" height="8" viewBox="0 0 24 20"><path d="M2 7c0-4 20-4 20 0v2h-5V7H7v2H2z M5 10h14l3 9H2z" fill="#fff"/></svg>
        <div class="small">020 7946 0123<br>020 7946 0124</div>
      </div>
      <div style="width:62px">
        <svg width="9" height="9" viewBox="0 0 24 24" fill="none" stroke="#fff" stroke-width="2"><circle cx="12" cy="12" r="10"/><ellipse cx="12" cy="12" rx="4" ry="10"/><path d="M2 12h20"/></svg>
        <div class="small">info@fernholtrail.co.uk<br>www.fernholtrail.co.uk</div>
      </div>
      <div style="width:48px">
        <svg width="7" height="9" viewBox="0 0 16 22"><path d="M8 0a8 8 0 0 1 8 8c0 6-8 14-8 14S0 14 0 8a8 8 0 0 1 8-8z" fill="#fff"/></svg>
        <div class="small">12 Harbour Row<br>Leeds LS1</div>
      </div>
    </div>
  </section>

  <!-- Business card back -->
  <section class="sheet card card-back">
    <div class="accent"></div>
    <div class="brand" style="left:0;right:0;justify-content:center;top:38px;font-size:17px">Fernhol Rail<span class="dot"></span></div>
  </section>

  <!-- Compliment slip -->
  <section class="sheet slip">
    <div class="accent"></div>
    <div class="brand" style="left:14px;top:24px;font-size:22px">Fernhol Rail<span class="dot"></span></div>
    <div class="address">12 Harbour Row, 4th floor, Leeds LS1</div>
    <div class="band">
      <div style="width:112px;border-radius:4px 0 0 4px"></div>
      <div class="url" style="width:172px;font-size:8px">www.fernholtrail.co.uk</div>
      <div style="width:117px;border-radius:0 4px 4px 0"></div>
    </div>
  </section>

  <!-- Envelope -->
  <section class="sheet envelope">
    <div class="flap"><span class="url" style="font-size:12px">www.fernholtrail.co.uk</span></div>
  </section>

</div>
</body>
</html>
```